We need a business card and letterhead design for an orthodontic office. Needs to be clean, simple and sleek

Target Market(s)

adults/children

Industry/Entity Type

Dental

Contact Information for Business Card

Logo that is attached

Font styles to use
Serif

Colors

Designer to choose colors to be used in the design.

Requirements
Must have
• Peter L Vantrell DDS
• Corinne Palk DMD
• 82 Tolland Avenue
• Merrick,NY 11903
• (516) 742-5096
• www.vantrellortho.example
Nice to have
• on the back.... space for appointment times
Should not have
• teeth

```html
<!DOCTYPE html>
<html lang="en">
<head>
<meta charset="utf-8">
<title>Peter Vantrell Orthodontics – Business Card</title>
<link rel="stylesheet" href="https://fonts.googleapis.com/css2?family=Arimo:wght@400;700&display=swap">
<style>
  :root {
    --page: #ffffff;
    --card: #2d2d2d;
    --accent: #5aa3cc;
    --ink-light: #ffffff;
    --ink-dark: #2d2d2d;
    --field: #ffffff;
  }
  * { margin: 0; padding: 0; box-sizing: border-box; }
  html, body { width: 1200px; height: 1000px; overflow: hidden; background: var(--page); }
  .canvas { position: relative; width: 1200px; height: 1000px; }

  .card { position: absolute; left: 339px; width: 522px; height: 300px; background: var(--card); }
  .card--front { top: 181px; }
  .card--back { top: 519px; }

  .wordmark { position: absolute; left: 33px; top: 92px; width: 200px; }
  .wordmark__mark { display: block; width: 14px; height: 14px; background: var(--accent); margin-bottom: 12px; }
  .wordmark__name {
    font-family: "Arimo", sans-serif; font-weight: 400;
    font-size: 22px; line-height: 28px; color: var(--ink-light);
  }

  .divider { position: absolute; left: 245px; top: 21px; width: 2px; height: 258px; background: var(--accent); }

  .contact {
    position: absolute; left: 284px; top: 84px;
    font-family: "Arimo", sans-serif; color: var(--ink-light);
    font-size: 16.5px; line-height: 21px;
  }
  .contact__doctor { font-weight: 700; font-size: 20px; line-height: 24px; }

  .appt { font-family: "Arimo", sans-serif; }
  .appt__name {
    position: absolute; left: 33px; top: 31px; width: 455px; height: 36px;
    background: var(--field); color: var(--ink-dark);
    font-size: 12.5px; line-height: 36px; padding-left: 8px;
  }
  .appt__label { position: absolute; top: 83px; color: var(--ink-light); font-size: 12.5px; }
  .appt__label--date { left: 41px; }
  .appt__label--time { left: 183px; }
  .appt__row { position: absolute; left: 33px; width: 455px; height: 36px; display: flex; }
  .appt__date { width: 136px; background: var(--accent); }
  .appt__remarks { flex: 1; background: var(--field); }
</style>
</head>
<body>
<div class="canvas">
  <section class="card card--front">
    <div class="wordmark">
      <span class="wordmark__mark"></span>
      <p class="wordmark__name">PETER<br>VANTRELL<br>ORTHODONTICS</p>
    </div>
    <div class="divider"></div>
    <div class="contact">
      <p class="contact__doctor">Peter L Vantrell DDS</p>
      <p>Corinne Palk DMD</p>
      <p>82 Tolland Avenue</p>
      <p>Merrick,NY 11903</p>
      <p>(516) 742-5096</p>
      <p>www.vantrellortho.example</p>
    </div>
  </section>

  <section class="card card--back appt">
    <div class="appt__name">NAME:</div>
    <span class="appt__label appt__label--date">DATE</span>
    <span class="appt__label appt__label--time">APPT TIME/ REMARKS</span>
    <div class="appt__row" style="top:107px"><div class="appt__date"></div><div class="appt__remarks"></div></div>
    <div class="appt__row" style="top:149px"><div class="appt__date"></div><div class="appt__remarks"></div></div>
    <div class="appt__row" style="top:191px"><div class="appt__date"></div><div class="appt__remarks"></div></div>
    <div class="appt__row" style="top:233px"><div class="appt__date"></div><div class="appt__remarks"></div></div>
  </section>
</div>
</body>
</html>
```